Software engineering company needs business card

I need a cool business card. Company: Soft Belan Brindlewood Ave 41 58207 Sincity Name: Gerald Vanholt CEO / Managing Director & Owner

```html
<!DOCTYPE html>
<html lang="en">
<head>
<meta charset="utf-8">
<title>Soft Belan – Business Card</title>
<link rel="stylesheet" href="https://fonts.googleapis.com/css2?family=Open+Sans:wght@400;600;700&display=swap">
<style>
  :root {
    --stage: #e9e7e4;
    --card-front: #ffffff;
    --card-back: #515253;
    --accent: #7dc242;
    --ink-dark: #4a4b4c;
    --ink-light: #ffffff;
    --deco: #626365;
    --deco-green: #5b6b4a;
  }
  * { box-sizing: border-box; margin: 0; padding: 0; }
  html, body {
    width: 1200px; height: 780px; overflow: hidden;
    background: var(--stage);
    font-family: "Open Sans", Arial, sans-serif;
  }
  .canvas {
    width: 1200px; height: 780px;
    display: flex; align-items: center; justify-content: center; gap: 60px;
  }
  .card {
    width: 525px; height: 300px;
    position: relative; overflow: hidden;
    box-shadow: 0 10px 30px rgba(0,0,0,.18);
  }
  .card--front {
    background: var(--card-front);
    display: flex; align-items: center; justify-content: center;
  }
  .brand { display: flex; align-items: center; gap: 14px; }
  .brand__mark { width: 22px; height: 22px; background: var(--accent); }
  .brand__name {
    font-size: 38px; font-weight: 600; letter-spacing: 6px;
    color: var(--ink-dark); text-transform: uppercase;
  }
  .card--back { background: var(--card-back); color: var(--ink-light); }
  .card__deco {
    position: absolute; right: 40px; top: 70px;
    width: 120px; height: 200px; border-radius: 6px;
    background: var(--deco);
  }
  .contact { position: absolute; left: 48px; top: 78px; }
  .contact__name { font-size: 20px; font-weight: 700; margin-bottom: 18px; }
  .contact__name-first { color: var(--accent); font-weight: 600; }
  .contact__address { font-size: 14px; line-height: 20px; margin-bottom: 10px; }
  .contact__row { display: flex; align-items: center; gap: 8px; font-size: 14px; line-height: 20px; }
  .contact__icon { width: 14px; height: 14px; background: var(--accent); display: block; }
</style>
</head>
<body>
<main class="canvas">
  <section class="card card--front">
    <div class="brand">
      <span class="brand__mark"></span>
      <span class="brand__name">Soft Belan</span>
    </div>
  </section>

  <section class="card card--back">
    <div class="card__deco" aria-hidden="true"></div>
    <div class="contact">
      <p class="contact__name"><span class="contact__name-first">Gerald</span> Vanholt</p>
      <p class="contact__address">Brindlewood Ave 41<br>58207 Sincity</p>
      <p class="contact__row">
        <svg class="contact__icon" viewBox="0 0 14 14" aria-hidden="true">
          <rect width="14" height="14" fill="#7dc242"/>
          <path d="M4 3h2l1 2.5-1.2 1a6 6 0 0 0 2.7 2.7l1-1.2L12 9v2a1 1 0 0 1-1 1A8 8 0 0 1 3 4a1 1 0 0 1 1-1z" fill="#515253"/>
        </svg>
        (01) 5550 4172
      </p>
      <p class="contact__row">
        <svg class="contact__icon" viewBox="0 0 14 14" aria-hidden="true">
          <rect width="14" height="14" fill="#7dc242"/>
          <rect x="2.5" y="4" width="9" height="6.5" fill="none" stroke="#515253" stroke-width="1.2"/>
          <path d="M2.5 4l4.5 3.5L11.5 4" fill="none" stroke="#515253" stroke-width="1.2"/>
        </svg>
        hello@softbelan.example
      </p>
    </div>
  </section>
</main>
</body>
</html>
```